Marketing flyer to advertise course vacancies

I am seeking something that is eye catching
A document that I can edit to list our courses and prices to try and gain further bookings on the courses.
I have attached our company logo, our website is www.brightpathskills.com.au for your viewing.
Our motto is Train today for a safer tomorrow, we would want this on the brochure.

```html
<!DOCTYPE html>
<html lang="en">
<head>
<meta charset="utf-8">
<title>BrightPath Skills Training – August Courses</title>
<link rel="stylesheet" href="https://fonts.googleapis.com/css2?family=Anton&family=Barlow+Semi+Condensed:wght@500;600;700&family=Poppins:wght@600;700&family=Stardos+Stencil:wght@700&display=swap">
<style>
  :root{
    --bg:#4a4a4a;
    --paper:#ffffff;
    --green:#1f7a3a;
    --green-head:#4a9140;
    --olive:#4f6e3a;
    --red:#d9262a;
    --orange:#f7901e;
    --ink:#1d1d1d;
    --muted:#5a5a5a;
    --foot-green:#1b6e3c;
    --hazard:#f2c014;
  }
  *{box-sizing:border-box;margin:0;padding:0}
  html,body{width:1026px;height:1200px;overflow:hidden;background:var(--bg)}
  .flyer{position:absolute;left:49px;top:0;width:928px;height:1200px;background:var(--paper);overflow:hidden;font-family:"Barlow Semi Condensed",sans-serif;color:var(--ink)}
  .brand{position:absolute;left:34px;top:60px;display:flex;align-items:center;gap:10px;width:150px;flex-wrap:wrap;justify-content:center}
  .brand-dot{width:46px;height:46px;border-radius:50%;background:var(--green)}
  .brand-name{width:100%;text-align:center;font-weight:700;font-size:20px;color:var(--green);line-height:1.05}
  .title{position:absolute;left:248px;top:32px;font-family:"Stardos Stencil",serif;font-weight:700;font-size:45px;line-height:40px;color:var(--green);letter-spacing:1px}
  .photo{position:absolute;right:0;top:0;width:380px;height:257px;background:radial-gradient(circle at 72% 40%,#ffd23a 0%,#f5a623 22%,#d8b89a 45%,#9aa0a4 70%,#6b6f72 100%)}
  .chevron{position:absolute;left:0;top:0;width:928px;height:257px}
  .motto{position:absolute;left:35px;top:188px;font-family:"Anton",sans-serif;font-size:41px;color:#fff;letter-spacing:-.5px;transform:scaleY(1.05)}
  .section-title{position:absolute;left:0;right:0;top:272px;text-align:center;font-family:"Poppins",sans-serif;font-weight:700;font-size:31px;color:var(--ink)}
  .table{position:absolute;left:33px;top:326px;width:860px}
  .row{display:grid;grid-template-columns:158px 364px 191px 122px;column-gap:8px}
  .head .cell{height:46px;border-radius:9px 9px 0 0;color:#fff;font-family:"Poppins",sans-serif;font-weight:600;font-size:20px;display:flex;align-items:center;justify-content:center}
  .head .c1{background:var(--green-head)}
  .head .c2{background:var(--red)}
  .head .c3{background:var(--olive)}
  .head .c4{background:var(--orange)}
  .body .cell{height:34.7px;box-shadow:0 2px 2px -1px rgba(0,0,0,.15);text-align:center;padding-top:4px}
  .code{font-weight:700;font-size:15.5px;line-height:18px}
  .name{font-weight:600;font-size:9.4px;line-height:12.5px;padding:0 14px}
  .when{font-weight:600;font-size:9.6px;line-height:11.5px}
  .cost{font-weight:700;font-size:15px;line-height:18px}
  .cost sup{font-size:8px;vertical-align:7px}
  .hazard{position:absolute;left:0;top:1083px;width:928px;height:14px;background:repeating-linear-gradient(-45deg,var(--hazard) 0 7px,#222 7px 14px)}
  .footer{position:absolute;left:0;top:1097px;width:928px;height:103px;background:#fff}
  .partner{position:absolute;left:34px;top:20px;width:290px;height:50px;background:#d3d3d3;border-radius:4px}
  .foot-green{position:absolute;left:0;top:0;width:928px;height:103px}
  .reserve{position:absolute;left:373px;top:6px;color:#fff;font-family:"Poppins",sans-serif;font-weight:600;font-size:16px;line-height:21px}
  .reserve .lead{color:var(--orange);font-weight:700}
  .reserve .line{display:flex;align-items:center;gap:6px}
  .reserve svg{width:9px;height:9px}
  .schedule{position:absolute;right:0;top:20px;width:270px;height:46px;background:var(--red);border-radius:23px 0 0 23px;color:#fff;font-family:"Poppins",sans-serif;font-weight:600;font-size:15px;line-height:18px;padding:5px 0 0 19px}
</style>
</head>
<body>
<div class="flyer">
  <header>
    <div class="photo" role="img" aria-label="Photo of a worker in a hi-vis vest using a fire extinguisher on flames"></div>
    <svg class="chevron" viewBox="0 0 928 257" aria-hidden="true">
      <polygon points="0,0 548,0 623,135 565,257 0,257" fill="#fff"/>
      <polyline points="548,0 623,135 565,257" fill="none" stroke="#d9262a" stroke-width="9"/>
      <polygon points="0,182 610,182 570,257 0,257" fill="#d9262a"/>
    </svg>
    <div class="brand"><span class="brand-dot"></span><span class="brand-name">BrightPath Skills</span></div>
    <h1 class="title">BRIGHTPATH<br>SKILLS<br>TRAINING</h1>
    <p class="motto">TRAIN TODAY FOR A SAFER TOMORROW</p>
  </header>

  <h2 class="section-title">UPCOMING AUGUST TRAINING COURSES</h2>

  <div class="table">
    <div class="row head"><div class="cell c1">CODE</div><div class="cell c2">TRAINING NAME</div><div class="cell c3">TIME &amp; DATE</div><div class="cell c4">COST</div></div>
    <div class="row body"><div class="cell code">TLILIC0003</div><div class="cell name">Licence to Operate a Forklift Truck – Formal Training &amp; Assessment (3 days)</div><div class="cell when">6, 7, &amp; 8 Aug (3days)<br>8.00am - 4.00pm</div><div class="cell cost"><sup>$</sup>525</div></div>
    <div class="row body"><div class="cell code">HLTAID011</div><div class="cell name">Provide First Aid inc HLTAID009 Provide CPR</div><div class="cell when">8th Aug<br>8.00am - 4.30pm</div><div class="cell cost"><sup>$</sup>125</div></div>
    <div class="row body"><div class="cell code">UETDREL006</div><div class="cell name">Working Safely Near Live Electrical Apparatus as a Non-Electrical Worker</div><div class="cell when">11th Aug<br>8.00am - 4.30pm</div><div class="cell cost"><sup>$</sup>225</div></div>
    <div class="row body"><div class="cell code">UETDRMP007</div><div class="cell name">Perform Rescue from a Live LV Panel inc HLTAID009 Provide cardiopulmonary resuscitation (LVR CPR)</div><div class="cell when">12th Aug<br>8.00am - 02.00pm</div><div class="cell cost"><sup>$</sup>100</div></div>
    <div class="row body"><div class="cell code">TLILIC0005</div><div class="cell name">Licence to Operate a EWP – Formal Training &amp; Assessment (3 days)</div><div class="cell when">13,14, &amp; 15th Aug<br>12:30 pm - 4:30 pm</div><div class="cell cost"><sup>$</sup>525</div></div>
    <div class="row body"><div class="cell code">RIIWHS202E</div><div class="cell name">Enter and Work in Confined Spaces and MSMWHS217 – Gas test atmospheres (combined)</div><div class="cell when">15th Aug<br>8.00am - 4.00pm</div><div class="cell cost"><sup>$</sup>300</div></div>
    <div class="row body"><div class="cell code">RIIWHS202E</div><div class="cell name">Enter and Work in Confined Spaces and MSMWHS217 – Gas test atmospheres (combined)</div><div class="cell when">15th Aug<br>8.00am - 4.30pm</div><div class="cell cost"><sup>$</sup>300</div></div>
    <div class="row body"><div class="cell code">RIIWHS204E</div><div class="cell name">Work Safely at Heights</div><div class="cell when">18th Aug<br>8.00am - 4.00pm</div><div class="cell cost"><sup>$</sup>225</div></div>
    <div class="row body"><div class="cell code">RIIWHS202E</div><div class="cell name">Enter and Work in Confined Spaces</div><div class="cell when">19th Aug<br>8.00am - 04.00pm</div><div class="cell cost"><sup>$</sup>225</div></div>
    <div class="row body"><div class="cell code">HLTAID011</div><div class="cell name">Provide First Aid inc HLTAID009 Provide CPR</div><div class="cell when">20th Aug<br>08:00 pm - 4:30 pm</div><div class="cell cost"><sup>$</sup>125</div></div>
    <div class="row body"><div class="cell code">CPCWHS1001</div><div class="cell name">Prepare to Work Safely in the Construction Industry (White Card) (Face to Face Training in QLD)</div><div class="cell when">21th Aug<br>8.00am - 04.00pm</div><div class="cell cost"><sup>$</sup>80</div></div>
    <div class="row body"><div class="cell code">CPCCLDG3001</div><div class="cell name">Licence to perform dogging training and assessment (5 days)</div><div class="cell when">18-22th Aug (5 days)<br>08:00 pm - 4:30 pm</div><div class="cell cost"><sup>$</sup>1450</div></div>
    <div class="row body"><div class="cell code">HLTPAT005</div><div class="cell name">Collect Specimens for Drugs of Abuse Testing</div><div class="cell when">22th Aug<br>8.00am - 12.00pm</div><div class="cell cost"><sup>$</sup>450</div></div>
    <div class="row body"><div class="cell code">MSMWHS216</div><div class="cell name">Operate Breathing Apparatus (Industrial)</div><div class="cell when">22th Aug<br>12:30 am - 4:30 pm</div><div class="cell cost"><sup>$</sup>200</div></div>
    <div class="row body"><div class="cell code">UETDREL006</div><div class="cell name">Working Safely Near Live Electrical Apparatus as a Non-Electrical Worker</div><div class="cell when">25th Aug<br>8.00am - 04.30pm</div><div class="cell cost"><sup>$</sup>225</div></div>
    <div class="row body"><div class="cell code">RIIMPO320F</div><div class="cell name">Conduct Civil Constructions Excavator Operations</div><div class="cell when">25 - 26 Aug (2days)<br>08:00 pm - 4:30 pm</div><div class="cell cost"><sup>$</sup>600</div></div>
    <div class="row body"><div class="cell code">UETDRMP007</div><div class="cell name">Perform Rescue from a Live LV Panel inc HLTAID009 Provide cardiopulmonary resuscitation (LVR CPR)</div><div class="cell when">26 Aug<br>08:00 pm - 02:00 pm</div><div class="cell cost"><sup>$</sup>100</div></div>
    <div class="row body"><div class="cell code">TLILIC0003</div><div class="cell name">Licence to Operate a Forklift Truck – Formal Training &amp; Assessment (3 days)</div><div class="cell when">27 - 29th Aug (3 days)<br>8.00am - 04.00pm</div><div class="cell cost"><sup>$</sup>525</div></div>
    <div class="row body"><div class="cell code">PUAFER005</div><div class="cell name">Operate as Part of an Emergency Control Organisation (Fire Warden)</div><div class="cell when">29 Aug<br>08:00 pm - 12:30 pm</div><div class="cell cost"><sup>$</sup>150</div></div>
    <div class="row body"><div class="cell code">CPPFES2005</div><div class="cell name">Demonstrate First Attack Firefighting Equipment</div><div class="cell when">29 Aug<br>12:30 am - 04:30 pm</div><div class="cell cost"><sup>$</sup>75</div></div>
  </div>

  <div class="hazard"></div>
  <footer class="footer">
    <svg class="foot-green" viewBox="0 0 928 103" aria-hidden="true"><polygon points="342,0 928,0 928,103 370,103" fill="#1b6e3c"/></svg>
    <div class="partner" role="img" aria-label="Partner badge"></div>
    <div class="reserve">
      <div class="lead">Reserve your seat now</div>
      <div class="line"><svg viewBox="0 0 10 10"><circle cx="5" cy="5" r="5" fill="#f7901e"/></svg>admin@brightpathskills.com.au</div>
      <div class="line"><svg viewBox="0 0 10 10"><circle cx="5" cy="5" r="5" fill="#f7901e"/></svg>07 5550 1234</div>
    </div>
    <div class="schedule">Full schedule at<br>www.brightpathskills.com.au</div>
  </footer>
</div>
</body>
</html>
```